Kettlelanternpress: Self-help book needs Promotional Postcard

Need a postcard 8.5" x 5.5" to promote my upcoming book. Its a self-help career book for women focusing on how the mother-daughter relationship impacts careers and tips and solutions for success. The model includes 5 different types of daughters.
Title: Where Did the Quiet Garden Lead Us?
Breathe new life into your career by understanding your mother daughter relationship.
Book release is January 9, 2017
Updates

I just uploaded 5 images of the daughter types without the words, better to use these, thanks! Added Thursday, December 29, 2016

Target Market(s)

This book is targeted towards women

Industry/Entity Type

Promotional

Font styles to use
Serif
Other font styles liked:
• see website text

Colors
00a990
ec252d
e34297

Requirements
Must have
• Eye catching promotional postcard. Must have image of book on front with title and subtitle, author name and website. I'd like images of the 5 daughters on the front.
• Colors should match the cover green and pink
• Back can have quotes and author bio
• can look at website (not quite completed) for more inspiration www.kettlelanternpress.example
Nice to have
• Curious to see how the postcard compliments the book and website.

```html
<!DOCTYPE html>
<html lang="en">
<head>
<meta charset="utf-8">
<title>Where Did the Quiet Garden Lead Us? – Postcard</title>
<link rel="stylesheet" href="https://fonts.googleapis.com/css2?family=Arimo:ital,wght@0,400;0,700;1,700&display=swap">
<style>
  :root {
    --page: #ffffff;
    --sage: #6c7a5c;
    --forest: #2d3d1b;
    --magenta: #a90a52;
    --ink: #000000;
    --white: #ffffff;
    --salmon: #f4aa9c;
  }
  * { box-sizing: border-box; margin: 0; padding: 0; }
  html, body {
    width: 1200px; height: 395px; overflow: hidden;
    background: var(--page);
    font-family: "Arimo", Arial, sans-serif;
  }
  .postcard-set { position: relative; width: 1200px; height: 395px; }

  /* Front */
  .front {
    position: absolute; left: 0; top: 0; width: 591px; height: 384px;
    background: var(--sage);
  }
  .front-panel {
    position: absolute; left: 17px; top: 24px; width: 553px; height: 262px;
    background: var(--magenta);
    border-bottom: 7px solid var(--ink);
  }
  .daughter-figure {
    position: absolute; left: 62px; top: 0; width: 150px; height: 255px;
    background: linear-gradient(90deg, #ffffff 0%, #f6dce6 55%, #111 56%, #000 100%);
  }
  .book-title {
    position: absolute; left: 235px; top: 34px; width: 305px;
    color: var(--white); font-weight: 700; font-style: italic;
    font-size: 24px; line-height: 30px; letter-spacing: 1px; text-align: center;
  }
  .book-subtitle {
    position: absolute; left: 240px; top: 160px; width: 300px;
    color: var(--white); font-weight: 700; font-style: italic;
    font-size: 13px; line-height: 16px; text-align: center;
  }
  .author-name {
    position: absolute; left: 0; top: 304px; width: 591px;
    color: var(--salmon); font-weight: 700; font-style: italic;
    font-size: 20px; letter-spacing: 2px; text-align: center;
  }
  .website {
    position: absolute; left: 0; top: 346px; width: 591px;
    color: var(--salmon); font-weight: 700;
    font-size: 19px; letter-spacing: 1.5px; text-align: center;
  }

  /* Back */
  .back {
    position: absolute; left: 607px; top: 0; width: 593px; height: 384px;
    background: var(--forest);
  }
  .endorsement {
    position: absolute; left: 20px; top: 14px; width: 553px;
    color: var(--salmon); font-weight: 700; text-align: center;
    font-size: 16.5px; line-height: 18px; letter-spacing: 1.4px;
  }
  .endorser {
    position: absolute; left: 20px; top: 128px; width: 553px;
    color: var(--white); font-size: 12px; line-height: 14px; text-align: center;
  }
  .endorser strong { color: var(--salmon); }
  .bio-panel {
    position: absolute; left: 36px; top: 170px; width: 545px; height: 201px;
    background: var(--magenta);
  }
  .author-photo {
    position: absolute; left: 11px; top: 9px; width: 126px; height: 186px;
    background: linear-gradient(160deg, #5d6b3a 0%, #8d7a58 45%, #4a1f24 100%);
  }
  .author-bio {
    position: absolute; left: 148px; top: 10px; width: 390px;
    color: var(--white); font-size: 13px; line-height: 15px; text-align: center;
  }
</style>
</head>
<body>
<main class="postcard-set">
  <section class="front">
    <div class="front-panel">
      <div class="daughter-figure" role="img" aria-label="Illustration of a woman's profile with long flowing white hair"></div>
      <h1 class="book-title">Where Did the Quiet Garden Lead Us?</h1>
      <p class="book-subtitle">Breathe new life into your career by understanding your mother daughter relationship.</p>
    </div>
    <p class="author-name">Miriam Halsey Dorane</p>
    <p class="website">www.kettlelanternpress.example</p>
  </section>

  <section class="back">
    <blockquote class="endorsement">“...Miriam draws the reader in with her poignant and insightful perspective of how family dynamics, particularly the conscious and subconscious aspects of the mother/daughter relationship, impact a career path and a fulfilled life...”</blockquote>
    <p class="endorser"><strong>Judge Renata Vellacourt, COURT HOUR,</strong><br>a syndicated TV court program.</p>
    <div class="bio-panel">
      <div class="author-photo" role="img" aria-label="Portrait photograph of the author outdoors among greenery"></div>
      <p class="author-bio">Miriam Halsey Dorane, M.A., M.Ed. is a clinical career counselor and licensed mental health counselor who has been helping clients make meaningful career transitions and address workplace challenges for over 26 years.<br>She is the 2013 recipient of the Outstanding Career Practitioner Award from the Northfield Career Guidance Society. ‘Quiet Garden’ integrates her expertise in career development with her training and insight about the adult mother-daughter relationship.</p>
    </div>
  </section>
</main>
</body>
</html>
```